Dietitian clinic needs a business card design

We need a business card design for a new dietitian group based in Singapore called "Lantern and Tide". We provide expert, personalised nutrition care to support a wide range of health needs, from chronic conditions to mindful eating. Our team also offers consulting, speaking, and tailored solutions for healthcare providers, organisations, and food services.

Target Market(s)

Adults

Industry/Entity Type

Healthcare

Contact Information for Business Card

Name, position, contact number, email, website address, our logo

Requirements
Nice to have
• Clean, professional but welcoming look

```html
<!DOCTYPE html>
<html lang="en">
<head>
<meta charset="utf-8">
<title>Lantern and Tide — Business Card</title>
<link rel="stylesheet" href="https://fonts.googleapis.com/css2?family=Playfair+Display:wght@800&family=Montserrat:wght@400;600&display=swap">
<style>
  :root {
    --backdrop: #999999;
    --paper: #ffffff;
    --blush: #dca0a1;
    --teal: #245a6b;
  }
  * { margin: 0; padding: 0; box-sizing: border-box; }
  html, body { width: 1068px; height: 1200px; overflow: hidden; }
  body { background: var(--backdrop); position: relative; font-family: "Montserrat", sans-serif; }

  .card {
    position: absolute;
    left: 155px;
    width: 758px;
    height: 432px;
    background: var(--paper);
    overflow: hidden;
  }
  .card--front { top: 112px; }
  .card--back { top: 654px; }

  .card__band {
    position: absolute;
    left: 0; bottom: 0;
    width: 100%;
    height: 66px;
    background: linear-gradient(to bottom, var(--blush) 0%, var(--blush) 25%, var(--teal) 70%, var(--teal) 100%);
  }

  .brand-mark {
    position: absolute;
    border: 5px solid var(--blush);
    border-radius: 50%;
  }
  .brand-name {
    position: absolute;
    font-family: "Playfair Display", serif;
    font-weight: 800;
    color: var(--blush);
    line-height: 0.9;
    text-align: center;
    letter-spacing: -0.5px;
  }

  .card--front .brand-mark { left: 331px; top: 68px; width: 96px; height: 96px; border-width: 6px; }
  .card--front .brand-name { left: 0; width: 100%; top: 188px; font-size: 62px; }

  .card--back .brand-mark { left: 423px; top: 77px; width: 54px; height: 54px; border-width: 4px; }
  .card--back .brand-name { left: 528px; top: 70px; width: 196px; font-size: 35px; }

  .accent-bar { position: absolute; left: 0; top: 92px; width: 27px; height: 59px; background: var(--blush); }
  .holder { position: absolute; left: 38px; top: 94px; color: var(--teal); }
  .holder__name { font-family: "Playfair Display", serif; font-weight: 800; font-size: 33px; line-height: 1; letter-spacing: 0.3px; }
  .holder__title { font-size: 16px; font-weight: 400; line-height: 1.1; margin-left: -1px; }

  .divider { position: absolute; left: 27px; top: 198px; width: 695px; height: 3px; background: var(--teal); }

  .contact-list { position: absolute; list-style: none; color: var(--teal); font-weight: 600; font-size: 20.5px; }
  .contact-list--left { left: 49px; top: 236px; }
  .contact-list li { display: flex; align-items: center; height: 42px; }
  .contact-icon { width: 22px; height: 22px; margin-right: 14px; flex: none; }
  .contact-icon circle { fill: var(--blush); }
  .contact-icon path { fill: none; stroke: #fff; stroke-width: 1.6; stroke-linecap: round; stroke-linejoin: round; }

  .address { position: absolute; left: 457px; top: 236px; display: flex; color: var(--teal); font-weight: 600; font-size: 20.5px; }
  .address .contact-icon { margin-top: 2px; margin-right: 14px; }
  .address__lines { line-height: 32.5px; margin-top: -4px; }
</style>
</head>
<body>

  <section class="card card--front" aria-label="Card front">
    <span class="brand-mark" aria-hidden="true"></span>
    <p class="brand-name">Lantern<br>and Tide</p>
    <div class="card__band" role="img" aria-label="Decorative pink and teal wave band"></div>
  </section>

  <section class="card card--back" aria-label="Card back">
    <span class="accent-bar" aria-hidden="true"></span>
    <div class="holder">
      <h1 class="holder__name">Your Name</h1>
      <p class="holder__title">Title</p>
    </div>

    <span class="brand-mark" aria-hidden="true"></span>
    <p class="brand-name">Lantern<br>and Tide</p>

    <span class="divider" aria-hidden="true"></span>

    <ul class="contact-list contact-list--left">
      <li>
        <svg class="contact-icon" viewBox="0 0 22 22" aria-hidden="true"><circle cx="11" cy="11" r="11"/><path d="M7.5 6.5 L9.5 6.5 L10.3 9 L9 10 C9.7 11.5 10.5 12.3 12 13 L13 11.7 L15.5 12.5 L15.5 14.5 C11 15 7 11 7.5 6.5Z"/></svg>
        012-345-6789
      </li>
      <li>
        <svg class="contact-icon" viewBox="0 0 22 22" aria-hidden="true"><circle cx="11" cy="11" r="11"/><path d="M6 8 H16 V14.5 H6Z M6 8 L11 12 L16 8"/></svg>
        info@website.com
      </li>
      <li>
        <svg class="contact-icon" viewBox="0 0 22 22" aria-hidden="true"><circle cx="11" cy="11" r="11"/><path d="M11 5.5 A5.5 5.5 0 1 0 11 16.5 A5.5 5.5 0 1 0 11 5.5 M5.5 11 H16.5 M11 5.5 C8.5 8 8.5 14 11 16.5 M11 5.5 C13.5 8 13.5 14 11 16.5"/></svg>
        www.website.com
      </li>
    </ul>

    <div class="address">
      <svg class="contact-icon" viewBox="0 0 22 22" aria-hidden="true"><circle cx="11" cy="11" r="11"/><path d="M11 17 C8 13.5 7 11.5 7 9.5 A4 4 0 0 1 15 9.5 C15 11.5 14 13.5 11 17Z M11 8 A1.5 1.5 0 1 0 11 11 A1.5 1.5 0 1 0 11 8"/></svg>
      <p class="address__lines">0000 Street<br>City<br>0000</p>
    </div>

    <div class="card__band" role="img" aria-label="Decorative pink and teal wave band"></div>
  </section>

</body>
</html>
```